Boutique Real Estate Brokerage looking for business card, letterhead and envelope design

We are looking for a cohesive design for our business cards, letterhead and envelopes and that mirrors our high-end homes and clientele. Fern & Gable is being launched and designed for the marketplace of tomorrow. We grew from the #1 team in our community into a full-service firm that is going to revolutionize the traditional real estate model.

We understand that it’s more important than ever to help our clients and partners adapt to behavioral and market changes being driven by generational shifts and technological advances in society, and by combining traditional brokerage services with innovative production and marketing capabilities, we know how to do that better than anyone else.

Requirements
Must have
• business card, letterhead and envelope design - attached logo.

```html
<!DOCTYPE html>
<html lang="en">
<head>
<meta charset="utf-8">
<title>Fern &amp; Gable Realty – Stationery</title>
<link rel="stylesheet" href="https://fonts.googleapis.com/css2?family=Montserrat:wght@600;700&family=Roboto:wght@400;500&family=Open+Sans:wght@400&display=swap">
<style>
  :root{
    --navy:#1f1a55;
    --gold:#b8844a;
    --paper:#ffffff;
    --sheet-tint:#f3f4f7;
    --ink:#3b3b45;
    --backdrop:#ece8e2;
    --faint:#e6e7ef;
  }
  *{margin:0;padding:0;box-sizing:border-box}
  html,body{width:1200px;height:3228px;overflow:hidden}
  body{background:var(--backdrop);position:relative;font-family:"Roboto",Arial,sans-serif;color:var(--navy)}
  .piece{position:absolute;background:var(--paper);box-shadow:0 6px 18px rgba(0,0,0,.18)}
  .brand{position:absolute;display:flex;align-items:center;gap:12px;font-family:"Montserrat",Arial,sans-serif;font-weight:700;color:var(--navy);white-space:nowrap}
  .brand-square{background:var(--navy);flex:none}
  .icon{width:14px;height:14px;fill:var(--navy);vertical-align:-2px;margin-right:6px}

  /* business card front */
  .card-front{left:239px;top:174px;width:763px;height:422px}
  .card-front .brand{left:81px;top:92px;font-size:32px}
  .card-front .brand-square{width:54px;height:54px}
  .holder{position:absolute;left:451px;top:100px;font-family:"Montserrat",Arial,sans-serif}
  .holder-name{font-weight:700;font-size:22px;color:var(--navy);text-transform:uppercase;line-height:1.05}
  .holder-role{font-weight:600;font-size:19px;color:var(--gold);line-height:1.2}
  .card-address{position:absolute;left:81px;top:270px;font-size:20px;line-height:27px;color:var(--ink)}
  .card-address strong{font-weight:400;color:var(--navy)}
  .card-contact{position:absolute;left:451px;top:268px;font-size:20px;line-height:27px;color:var(--ink);list-style:none}
  .card-contact .icon{width:18px;height:18px}

  /* business card back */
  .card-back{left:239px;top:686px;width:763px;height:423px;background:var(--navy)}
  .card-back .brand{left:133px;top:170px;font-size:46px;color:#fff;gap:18px}
  .card-back .brand-square{width:78px;height:78px;background:var(--gold)}

  /* letterhead */
  .letterhead{left:234px;top:1385px;width:725px;height:941px;background:linear-gradient(#fff 0%,var(--sheet-tint) 30%,var(--sheet-tint) 65%,#fff 100%)}
  .letterhead .brand{left:64px;top:82px;font-size:24px;gap:10px}
  .letterhead .brand-square{width:40px;height:40px}
  .letter-body{position:absolute;left:64px;top:223px;width:596px;font-family:"Open Sans",Arial,sans-serif;font-size:12px;line-height:18px;color:var(--ink);text-align:justify}
  .letter-body p{margin-bottom:18px}
  .signature{position:absolute;left:84px;top:653px;width:70px;height:56px;background:linear-gradient(135deg,#dcdce2,#f3f4f7)}
  .watermark{position:absolute;background:var(--faint);opacity:.7}
  .letterhead .watermark{right:0;bottom:0;width:160px;height:170px}
  .footer{position:absolute;display:flex;gap:16px;font-size:12px;line-height:17px;color:var(--ink)}
  .footer ul{list-style:none}
  .footer .icon{width:11px;height:11px;margin-right:3px}
  .footer strong{font-weight:500;color:var(--navy)}
  .footer-bar{position:absolute;left:0;width:18px;height:44px;background:var(--navy)}
  .letterhead .footer{left:64px;top:841px}
  .letterhead .footer-bar{top:844px}

  /* envelope front */
  .envelope-front{left:264px;top:2414px;width:683px;height:339px}
  .envelope-front .brand{left:44px;top:38px;font-size:24px;gap:10px}
  .envelope-front .brand-square{width:40px;height:40px}
  .envelope-front .watermark{right:0;bottom:0;width:140px;height:185px}
  .envelope-front .footer{left:44px;top:251px}
  .envelope-front .footer-bar{top:253px}

  /* envelope back */
  .envelope-back{left:264px;top:2796px;width:683px;height:342px;overflow:hidden}
  .envelope-flap{position:absolute;left:0;top:0;width:683px;height:104px}
  .envelope-back .brand{left:264px;top:37px;font-size:15px;color:#fff;gap:7px}
  .envelope-back .brand-square{width:26px;height:26px;background:var(--gold)}
</style>
</head>
<body>
<svg width="0" height="0" style="position:absolute" aria-hidden="true">
  <symbol id="i-phone" viewBox="0 0 24 24"><path d="M6.6 10.8a15 15 0 0 0 6.6 6.6l2.2-2.2a1 1 0 0 1 1-.25 11 11 0 0 0 3.6.6 1 1 0 0 1 1 1V20a1 1 0 0 1-1 1A17 17 0 0 1 3 4a1 1 0 0 1 1-1h3.5a1 1 0 0 1 1 1c0 1.25.2 2.45.6 3.6a1 1 0 0 1-.25 1z"/></symbol>
  <symbol id="i-mail" viewBox="0 0 24 24"><path d="M2 5h20v14H2z M2 5l10 8 10-8" /><path d="M3 6.5l9 7 9-7V18H3z" fill="#fff" opacity=".35"/></symbol>
  <symbol id="i-globe" viewBox="0 0 24 24"><path d="M12 2a10 10 0 1 0 0 20 10 10 0 0 0 0-20zm-1 17.9A8 8 0 0 1 4.1 11H7c.2 3.2 1.7 6.3 4 8.9zm2 0c2.3-2.6 3.8-5.7 4-8.9h2.9a8 8 0 0 1-6.9 8.9zM17 9c-.2-2.4-1.3-4.8-3-6.8A8 8 0 0 1 19.9 9zM12 3.6C13.7 5.4 14.8 7.2 15 9H9c.2-1.8 1.3-3.6 3-5.4zM7 9H4.1A8 8 0 0 1 10 2.2C8.3 4.2 7.2 6.6 7 9zm2 2h6c-.2 2.6-1.2 5-3 7.3-1.8-2.3-2.8-4.7-3-7.3z"/></symbol>
</svg>

<!-- Business card, front -->
<section class="piece card-front" aria-label="Business card front">
  <div class="brand"><span class="brand-square"></span>Fern &amp; Gable</div>
  <div class="holder">
    <p class="holder-name">Daniel Whitford</p>
    <p class="holder-role">Managing Director</p>
  </div>
  <address class="card-address" style="font-style:normal">
    <strong>Fern &amp; Gable Realty LTD.</strong><br>
    48 Maple Crest Road,<br>
    Oakridge, ON K2B 7P4
  </address>
  <ul class="card-contact">
    <li><svg class="icon"><use href="#i-phone"/></svg>555.214.0187</li>
    <li><svg class="icon"><use href="#i-mail"/></svg>info@fernandgable.com</li>
    <li><svg class="icon"><use href="#i-globe"/></svg>www.fernandgable.com</li>
  </ul>
</section>

<!-- Business card, back -->
<section class="piece card-back" aria-label="Business card back">
  <div class="brand"><span class="brand-square"></span>Fern &amp; Gable</div>
</section>

<!-- Letterhead -->
<section class="piece letterhead" aria-label="Letterhead">
  <div class="brand"><span class="brand-square"></span>Fern &amp; Gable</div>
  <div class="letter-body">
    <p>Dear customer,</p>
    <p>Lorem ipsum dolor sit amet, consectetur adipisicing elit, sed do eiusmod tempor incididunt ut labore et dolore magna aliqua. Ut enim ad minim veniam, quis nostrud exercitation ullamco laboris nisi ut aliquip ex ea commodo consequat. Duis aute irure dolor in reprehenderit in voluptate velit esse cillum dolore eu fugiat nulla pariatur. Excepteur sint occaecat cupidatat non proident, sunt in culpa qui officia deserunt mollit anim id est laborum.</p>
    <p>Lorem ipsum dolor sit amet, consectetur adipisicing elit, sed do eiusmod tempor incididunt ut labore et dolore magna aliqua. Ut enim ad minim veniam, quis nostrud exercitation ullamco laboris nisi ut aliquip ex ea commodo consequat. Duis aute irure dolor in reprehenderit in voluptate velit esse cillum dolore eu fugiat nulla pariatur. Excepteur sint occaecat cupidatat non proident, sunt in culpa qui officia deserunt mollit anim id est laborum.</p>
    <p>Lorem ipsum dolor sit amet, consectetur adipisicing elit, sed do eiusmod tempor incididunt ut labore et dolore magna aliqua. Ut enim ad minim veniam, quis nostrud exercitation ullamco laboris nisi ut aliquip ex ea commodo consequat. Duis aute irure dolor in reprehenderit in voluptate velit esse cillum dolore eu fugiat nulla pariatur. Excepteur sint occaecat cupidatat non proident, sunt in culpa qui officia deserunt mollit anim id est laborum.</p>
    <p>Lorem ipsum dolor sit amet, consectetur adipisicing elit, sed do eiusmod tempor incididunt ut labore et dolore magna aliqua. Ut enim ad minim veniam, quis nostrud exercitation ullamco laboris nisi ut aliquip ex ea commodo consequat. Duis aute irure dolor in reprehenderit.</p>
    <p>Yours Sincerely,</p>
  </div>
  <div class="signature" role="img" aria-label="Handwritten signature"></div>
  <div class="watermark" aria-hidden="true"></div>
  <span class="footer-bar" aria-hidden="true"></span>
  <div class="footer">
    <ul>
      <li><svg class="icon"><use href="#i-phone"/></svg>555.214.0187</li>
      <li><svg class="icon"><use href="#i-mail"/></svg>info@fernandgable.com</li>
      <li><svg class="icon"><use href="#i-globe"/></svg>www.fernandgable.com</li>
    </ul>
    <ul>
      <li><strong>Fern &amp; Gable Realty LTD</strong></li>
      <li>48 Maple Crest Road,</li>
      <li>Oakridge, ON K2B 7P4</li>
    </ul>
  </div>
</section>

<!-- Envelope, front -->
<section class="piece envelope-front" aria-label="Envelope front">
  <div class="brand"><span class="brand-square"></span>Fern &amp; Gable</div>
  <div class="watermark" aria-hidden="true"></div>
  <span class="footer-bar" aria-hidden="true"></span>
  <div class="footer">
    <ul>
      <li><svg class="icon"><use href="#i-phone"/></svg>555.214.0187</li>
      <li><svg class="icon"><use href="#i-mail"/></svg>info@fernandgable.com</li>
      <li><svg class="icon"><use href="#i-globe"/></svg>www.fernandgable.com</li>
    </ul>
    <ul>
      <li><strong>Fern &amp; Gable Realty LTD</strong></li>
      <li>48 Maple Crest Road,</li>
      <li>Oakridge, ON K2B 7P4</li>
    </ul>
  </div>
</section>

<!-- Envelope, back -->
<section class="piece envelope-back" aria-label="Envelope back">
  <svg class="envelope-flap" viewBox="0 0 683 104" aria-hidden="true">
    <path d="M0 0H683L672 84Q669 101 652 101H31Q14 101 11 84Z" fill="var(--navy)"/>
  </svg>
  <div class="brand"><span class="brand-square"></span>Fern &amp; Gable</div>
</section>
</body>
</html>
```